Crestline Podiatry Needs a Branded 8.5 x 11 template

We need a single template that will reflect our brand and have a really interesting and catchy feel. Be creative. It should include our logo a catch phrase like "Where Your Feet Are in Good Hands" and editable. There should be a header with this information. The central portion should be available to place text about medical conditions or other information and available to take pictures.
The footer needs to be all of the info on our location such as address, phone, drs names etc. - see must haves
We like shadows, 3D, really creative and catchy.
Below is an example that my friend uses. I like it but would like something a little more interesting. I do not want the same design as the flyer attached.
Logo is attached.
Our Colors: Want plenty of white space
#FAC000
#9F38AA

Target Market(s)

Patients and Physicians. We are podiatrists, foot and ankle specialists but I do not want any pictures of feet or medical stuff on the template.

Industry/Entity Type

Medical

Requirements
Must have
• For the Footer: Make it creative please

Physicians and Surgeons of the Foot and Ankle
Dr. Owen Brellis
Dr. Harriet Vandermolen
Address 4187 N. Corliss Blvd. Suite 508, Tampa, FL 33614
phone - 813-462-0197
email office@crestlinepodiatrygroup.net
web http://www.theGulfsideFootClinic.net

The Tagline section in the header needs to be editable so I can make changes. The middle section also needs to be editable.

I prefer to make edits in Photoshop or possibly Illustrator

```html
<!DOCTYPE html>
<html lang="en">
<head>
<meta charset="utf-8">
<title>Crestline Podiatry Letterhead</title>
<link rel="stylesheet" href="https://fonts.googleapis.com/css2?family=Righteous&family=Tinos:ital,wght@0,400;0,700;1,700&family=Poppins:wght@300;500&display=swap">
<style>
  :root {
    --backdrop: #e4e1e5;
    --paper: #fbfbfb;
    --band-light: #fbd6f4;
    --band-deep: #e7a3e3;
    --plum: #5b1f6a;
    --violet: #a659b6;
    --ink: #222;
    --orange: #f47a20;
    --orange-dark: #d85a12;
    --green: #8fc96a;
    --yellow: #e2b42a;
    --sky: #4fc1ec;
    --pink: #f7bfe0;
    --peach: #fbcc93;
    --icon: #555;
  }
  * { box-sizing: border-box; margin: 0; padding: 0; }
  html, body { width: 1200px; height: 675px; overflow: hidden; background: var(--backdrop); }
  .sheet {
    position: absolute; left: 339px; top: 0; width: 522px; height: 675px;
    background: var(--paper); box-shadow: 0 0 14px rgba(0,0,0,.18); overflow: hidden;
  }
  .header-band {
    position: absolute; left: 15px; top: 8px; width: 492px; height: 66px;
    background: linear-gradient(90deg, var(--band-light), var(--band-deep) 55%, var(--band-light));
  }
  .header-flower {
    position: absolute; left: 15px; top: 8px; width: 62px; height: 66px;
    background: linear-gradient(160deg, #ffffff 0%, #fdf3c8 45%, #f6d2ee 100%);
  }
  .tagline {
    position: absolute; left: 100px; top: 24px; font-family: "Righteous", sans-serif;
    font-size: 20px; line-height: 20px; color: var(--plum); letter-spacing: .6px; text-transform: uppercase;
  }
  .brand {
    position: absolute; left: 366px; top: 32px; display: flex; align-items: center; gap: 6px;
    font-family: "Tinos", serif; font-size: 15px; color: var(--plum);
  }
  .brand-dot { width: 10px; height: 10px; border-radius: 50%; background: var(--violet); }
  .section-title {
    position: absolute; left: 100px; top: 99px; font-family: "Poppins", sans-serif; font-weight: 300;
    font-size: 12.5px; color: var(--violet); letter-spacing: .6px;
  }
  .article {
    position: absolute; left: 100px; top: 124px; width: 396px; font-family: "Tinos", serif;
    font-size: 9.3px; line-height: 14.2px; color: var(--ink); text-align: justify;
  }
  .article em { font-weight: 700; font-style: italic; }
  .page-curl {
    position: absolute; left: 397px; top: 490px; width: 110px; height: 6px;
    background: linear-gradient(90deg, transparent, #bbb); border-radius: 50%; filter: blur(2px);
  }
  .footer-art {
    position: absolute; left: 0; top: 440px; width: 190px; height: 235px;
    background: radial-gradient(ellipse at 30% 62%, #e8432f 0 16%, transparent 45%),
                radial-gradient(ellipse at 62% 45%, #f3a33a 0 14%, transparent 40%),
                radial-gradient(ellipse at 22% 35%, #8d3fa5 0 11%, transparent 38%),
                radial-gradient(ellipse at 70% 82%, #4aa3d8 0 10%, transparent 35%),
                linear-gradient(transparent, #f4d1e6);
  }
  .footer-tab {
    position: absolute; left: 195px; top: 522px; width: 22px; height: 29px; background: var(--orange-dark);
    box-shadow: 2px 2px 3px rgba(0,0,0,.25);
  }
  .footer-heading {
    position: absolute; left: 212px; top: 527px; width: 295px; height: 19px; background: var(--orange);
    color: #fff; font-family: "Poppins", sans-serif; font-weight: 500; font-size: 10.5px; line-height: 19px; padding-left: 18px;
  }
  .contact-list { position: absolute; left: 254px; top: 557px; list-style: none; }
  .contact-list li {
    position: relative; width: 253px; height: 14px; margin-bottom: 6px; padding-left: 8px;
    font-family: "Tinos", serif; font-size: 10px; line-height: 14px; color: #444;
  }
  .contact-list svg { position: absolute; left: -20px; top: 0; width: 14px; height: 14px; }
  .c-doctors { background: var(--green); }
  .c-address { background: var(--yellow); }
  .c-phone { background: var(--sky); }
  .c-email { background: var(--pink); }
  .c-web { background: var(--peach); }
</style>
</head>
<body>
<main class="sheet">
  <header>
    <div class="header-band"></div>
    <div class="header-flower" role="img" aria-label="White daisy illustration"></div>
    <p class="tagline">“ Where your feet<br>are in good hands ”</p>
    <div class="brand"><span class="brand-dot"></span>Crestline Podiatry</div>
  </header>

  <section>
    <h2 class="section-title">DO YOU KNOW ~</h2>
    <p class="article">…bunions are not necessarily a foot condition that afflicts older people? Did you know that <em>bunions can also develop early in children?</em> Juvenile bunions are not uncommon, and can potentially be a source of significant discomfort to children. An early developing bunion can be present for a wide variety of reasons. Traditionally, a typical bunion develops after many years of walking with a flat foot as the strain of flattening feet eventually force the big toe joint to deform. When a bunion develops early in kids, the process is a little different. It is probably a combination of the position of the developing child in the womb influencing bone growth, parental genetics, and the presence of foot structural problems that lead to this early development. There are also other factors, which include growth abnormalities in the position of either the long bone or the toe bone that influence the position of the bunion. An unstable foot structure, which includes excessively loose flat feet and feet with tight Achilles tendons, contributes to the acceleration of bunion formation. Another condition, metatarsus adductus, can lead to early bunions. This condition is seen when all the long metatarsal bones are angled inward towards the big toe. This condition is fairly frequent (one in every thousand births), and because the big metatarsal bone is angled inward already in this condition, the ingredient for a bunion to form is already there.<br>The <em>treatment of bunions in kids is a little different than treatment for adults</em>. In adults, except when not possible due to health issues, the typical treatment is surgical correction. Because children are still growing bone, surgery to return the bone to its proper position may not lead to a long term correction. Unless a childs bunion is very painful and limiting activity, it is best to conservatively treat a bunion and delay surgery until after the bone starts to mature (near the start of the teen years). This conservative treatment includes wider shoes to avoid pressure on the bunion bump, stretching to keep the Achilles tendon limber, and prescription orthotic inserts to stabilize flat feet. When the time is right for surgery, the same procedures that are used for adults are considered in kids. However, due to the severity of an early developing bunion, more extensive surgery may be needed that requires a slightly longer healing time. <em>If your child has a bunion, it may be well worth your time to have him/her evaluated by a foot specialist to determine if future treatment is needed.</em></p>
    <div class="page-curl"></div>
  </section>

  <footer>
    <div class="footer-art" role="img" aria-label="Colourful abstract flower illustration"></div>
    <div class="footer-tab"></div>
    <h3 class="footer-heading">Physicians and Surgeons of the Foot and Ankle</h3>
    <ul class="contact-list">
      <li class="c-doctors"><svg viewBox="0 0 16 16"><circle cx="8" cy="5" r="3" fill="var(--icon)"/><path d="M2 15c0-4 3-6 6-6s6 2 6 6z" fill="var(--icon)"/></svg>Dr. Owen Brellis &nbsp;|&nbsp; Dr. Harriet Vandermolen</li>
      <li class="c-address"><svg viewBox="0 0 16 16"><path d="M3 1v14" stroke="var(--icon)" stroke-width="1.5"/><path d="M3.5 2h10l-3 3 3 3h-10z" fill="var(--icon)"/></svg>4187 N. Corliss Blvd. Suite 508, Tampa, FL 33614</li>
      <li class="c-phone"><svg viewBox="0 0 16 16"><path d="M4 1l3 3-2 2c1 2 3 4 5 5l2-2 3 3-2 3C7 15 1 9 1 3z" fill="var(--icon)"/></svg>813-462-0197</li>
      <li class="c-email"><svg viewBox="0 0 16 16"><rect x="1" y="3" width="14" height="10" fill="none" stroke="var(--icon)" stroke-width="1.5"/><path d="M1 3l7 6 7-6" fill="none" stroke="var(--icon)" stroke-width="1.5"/></svg>office@crestlinepodiatrygroup.net</li>
      <li class="c-web"><svg viewBox="0 0 16 16"><circle cx="8" cy="8" r="6.5" fill="none" stroke="var(--icon)" stroke-width="1.5"/><ellipse cx="8" cy="8" rx="3" ry="6.5" fill="none" stroke="var(--icon)"/><path d="M1.5 8h13" stroke="var(--icon)"/></svg>www.theGulfsideFootClinic.net</li>
    </ul>
  </footer>
</main>
</body>
</html>
```